NEW Modern Sleek Business Card for VR Language Startup

Our startup is using VR to lead the next wave of world language education. We need a two-sided business card that introduces the larger organization (Brightvale Tongues Inc) and our contact info on one side and shows the product, Lexiquorra, on the other side.

Side 1 (contact info)= Brightvale Logo and Contact info (name, title, phone, email)

Side 2 (product)= Lexiquora logo, text, and website
Text= Culturally Immersive Language Learning Games
Website= www.lexiquora-demo.test

Target Market(s)

Education, Technology

Contact Information for Business Card

Contact info will be updated upon approval of the design. For now, put this as a placeholder.

Peter Hallow
Founder & CEO
phallow@mailbox-demo.test
(555)-010-4477

Font styles to use
Other font styles liked:
• Gibson and Century Gothic are the brand fonts

Requirements
Nice to have
• I would love to see cohesion between the design and colors of the two logos. I have attached a few business card designs that I like, so you can get a feel for my preferred style.

```html
<!DOCTYPE html>
<html lang="en">
<head>
<meta charset="utf-8">
<title>Brightvale Tongues – Business Card</title>
<link rel="stylesheet" href="https://fonts.googleapis.com/css2?family=Poppins:wght@400;500;600;700&display=swap">
<style>
  :root {
    --page-bg: #e9eaee;
    --card-bg: #ffffff;
    --ink: #1d1d22;
    --ink-soft: #4a4a52;
    --divider: #b9b9c0;
    --product-blue: #3d7cf2;
    --cyan: #2fd3e6;
    --blue: #4a6cf7;
    --purple: #8a3ff0;
    --red: #f0304f;
    --orange: #f7762a;
  }
  * { box-sizing: border-box; margin: 0; padding: 0; }
  html, body {
    width: 1200px; height: 1200px; overflow: hidden;
    background: var(--page-bg);
    font-family: "Poppins", sans-serif;
    color: var(--ink);
  }
  .canvas {
    width: 1200px; height: 1200px;
    display: flex; flex-direction: column; align-items: center; justify-content: center;
    gap: 44px;
  }
  .card {
    position: relative;
    width: 900px; height: 514px;
    background: var(--card-bg);
    box-shadow: 0 10px 30px rgba(0,0,0,0.12);
    overflow: hidden;
  }

  /* Product side */
  .product-card .edge-line {
    position: absolute; top: 0; bottom: 0; right: 34px; width: 2px;
    background: linear-gradient(to bottom, var(--cyan), var(--blue));
  }
  .product-logo {
    position: absolute; left: 0; right: 0; top: 150px;
    display: flex; align-items: center; justify-content: center; gap: 22px;
  }
  .logo-dot {
    width: 86px; height: 86px; border-radius: 50%;
    background: var(--product-blue);
  }
  .product-name {
    font-size: 64px; font-weight: 600; letter-spacing: -0.5px;
    color: var(--product-blue);
  }
  .product-tagline {
    position: absolute; left: 0; right: 0; top: 300px;
    display: flex; align-items: center; justify-content: center; gap: 18px;
    font-size: 21px; font-weight: 500; color: var(--ink-soft); letter-spacing: 0.3px;
  }
  .tagline-rule {
    width: 90px; height: 2px;
    background: linear-gradient(to right, var(--blue), var(--purple));
  }
  .product-web {
    position: absolute; left: 0; right: 0; top: 346px;
    text-align: center; font-size: 19px; color: var(--ink-soft);
  }

  /* Contact side */
  .contact-card .color-band {
    position: absolute; left: 0; right: 0; bottom: 0; height: 18px;
    background: linear-gradient(to right, var(--orange), var(--red), var(--purple), var(--blue), var(--cyan));
  }
  .company-logo {
    position: absolute; left: 70px; top: 210px;
    display: flex; align-items: center; gap: 20px;
  }
  .company-logo .logo-dot {
    width: 78px; height: 78px;
    background: var(--red);
  }
  .company-name {
    font-size: 46px; font-weight: 600; color: var(--ink); letter-spacing: 1px;
  }
  .column-divider {
    position: absolute; left: 478px; top: 130px; width: 2px; height: 215px;
    background: var(--divider);
  }
  .contact-info {
    position: absolute; left: 518px; top: 128px;
  }
  .person-name {
    font-size: 32px; font-weight: 700; letter-spacing: 0.5px;
    background: linear-gradient(to right, var(--orange), var(--red), var(--purple), var(--cyan));
    -webkit-background-clip: text; background-clip: text; color: transparent;
  }
  .person-title {
    font-size: 18px; color: var(--ink-soft); margin-top: 2px; margin-bottom: 16px;
  }
  .contact-list { list-style: none; }
  .contact-list li {
    display: flex; align-items: center; gap: 14px;
    font-size: 19px; color: var(--ink); margin-bottom: 8px;
  }
  .contact-icon { width: 20px; height: 20px; flex: none; }
</style>
</head>
<body>
<main class="canvas">

  <section class="card product-card">
    <div class="edge-line"></div>
    <div class="product-logo">
      <span class="logo-dot"></span>
      <span class="product-name">Lexiquora</span>
    </div>
    <div class="product-tagline">
      <span class="tagline-rule"></span>
      <span>Culturally Immersive Language Learning Games</span>
      <span class="tagline-rule"></span>
    </div>
    <div class="product-web">www.lexiquora-demo.test</div>
  </section>

  <section class="card contact-card">
    <div class="company-logo">
      <span class="logo-dot"></span>
      <span class="company-name">Brightvale</span>
    </div>
    <div class="column-divider"></div>
    <div class="contact-info">
      <h1 class="person-name">PETER HALLOW</h1>
      <p class="person-title">Founder &amp; CEO</p>
      <ul class="contact-list">
        <li>
          <svg class="contact-icon" viewBox="0 0 24 24" aria-hidden="true">
            <path d="M6.6 10.8a15 15 0 0 0 6.6 6.6l2.2-2.2a1 1 0 0 1 1-.25 11.4 11.4 0 0 0 3.6.57 1 1 0 0 1 1 1V20a1 1 0 0 1-1 1A17 17 0 0 1 3 4a1 1 0 0 1 1-1h3.5a1 1 0 0 1 1 1c0 1.25.2 2.45.57 3.6a1 1 0 0 1-.25 1z" fill="var(--orange)"/>
          </svg>
          <span>(555)-010-4477</span>
        </li>
        <li>
          <svg class="contact-icon" viewBox="0 0 24 24" aria-hidden="true">
            <rect x="2.5" y="5" width="19" height="14" rx="1.5" fill="none" stroke="var(--red)" stroke-width="2"/>
            <path d="M3 6l9 7 9-7" fill="none" stroke="var(--red)" stroke-width="2"/>
          </svg>
          <span>phallow@mailbox-demo.test</span>
        </li>
        <li>
          <svg class="contact-icon" viewBox="0 0 24 24" aria-hidden="true">
            <circle cx="12" cy="12" r="9" fill="none" stroke="var(--purple)" stroke-width="2"/>
            <ellipse cx="12" cy="12" rx="4" ry="9" fill="none" stroke="var(--purple)" stroke-width="1.6"/>
            <path d="M3 12h18" stroke="var(--purple)" stroke-width="1.6"/>
          </svg>
          <span>www.lexiquora-demo.test</span>
        </li>
      </ul>
    </div>
    <div class="color-band"></div>
  </section>

</main>
</body>
</html>
```